Business card for psychiatrist

Business card design project for a psychiatristWe would like to have the impression of 1. We (patient and the doctor) are working together.2. Light the way so that patients can see where they are going and what their goals are.3. One side of the business card will have the letter "TFP" which stands for Thornvale Family Psychiatry.4. The other side of the business card will have the address, phone number, name of the psychiatrist, website, etc.5. A logo could go into either side of the business card. Let's see what looks better.
Business card design project for a psychiatrist
We would like to have the impression of
1. We (patient and the doctor) are working together.
2. Light the way so that patients can see where they are going and what their goals are.
3. One side of the business card will have the letter "TFP" which stands for Thornvale Family Psychiatry.
4. The other side of the business card will have the address, phone number, name of the psychiatrist, website, etc.
5. A logo could go into either side of the business card. Let's see what looks better.
Colors
Designer to choose colors to be used in the design.
Look and feel
Each slider illustrates characteristics of the customer's brand and the style your logo design should communicate.

```html
<!DOCTYPE html>
<html lang="en">
<head>
<meta charset="utf-8">
<title>Thornvale Family Psychiatry – Business Card</title>
<link rel="stylesheet" href="https://fonts.googleapis.com/css2?family=Work+Sans:wght@400;500;600&display=swap">
<style>
  :root {
    --page-bg: #1c1c1c;
    --card-bg: #262626;
    --card-edge: #303030;
    --brand-blue: #29a9e1;
    --accent-orange: #f7931e;
    --text-light: #f2f2f2;
    --mark-grey: #cfcfcf;
  }
  * { margin: 0; padding: 0; box-sizing: border-box; }
  html, body {
    width: 1200px;
    height: 900px;
    overflow: hidden;
    background: var(--page-bg);
    font-family: "Work Sans", Arial, sans-serif;
  }
  .canvas {
    width: 1200px;
    height: 900px;
    display: flex;
    flex-direction: column;
    align-items: center;
    justify-content: center;
    gap: 40px;
  }
  .card {
    width: 700px;
    height: 400px;
    background: var(--card-bg);
    border: 1px solid var(--card-edge);
    position: relative;
  }
  /* Back side */
  .card-back {
    display: flex;
    align-items: center;
    justify-content: center;
  }
  .back-monogram {
    font-size: 150px;
    font-weight: 600;
    letter-spacing: 6px;
    color: var(--mark-grey);
  }
  /* Front side */
  .card-front {
    display: flex;
    align-items: center;
    padding: 0 48px;
  }
  .brand {
    width: 300px;
    color: var(--brand-blue);
    font-weight: 600;
  }
  .brand-initials {
    font-size: 104px;
    line-height: 1;
    letter-spacing: 4px;
  }
  .brand-name {
    margin-top: 10px;
    font-size: 15.5px;
    letter-spacing: 1.2px;
    text-transform: uppercase;
  }
  .divider {
    width: 2px;
    height: 200px;
    background: var(--brand-blue);
    margin: 0 34px 0 16px;
  }
  .contact { color: var(--text-light); }
  .person-name {
    font-size: 26px;
    font-weight: 500;
    letter-spacing: 2px;
    text-transform: uppercase;
    color: var(--brand-blue);
  }
  .person-role {
    font-size: 17px;
    margin-bottom: 18px;
  }
  .address {
    font-size: 17px;
    line-height: 1.4;
    margin-bottom: 14px;
  }
  .contact-line {
    display: flex;
    align-items: center;
    gap: 8px;
    font-size: 17px;
    line-height: 1.5;
  }
  .contact-line svg { width: 13px; height: 13px; flex: none; }
  .web-domain { color: var(--brand-blue); }
</style>
</head>
<body>
<main class="canvas">
  <section class="card card-back" aria-label="Card back">
    <div class="back-monogram">TFP</div>
  </section>

  <section class="card card-front" aria-label="Card front">
    <div class="brand">
      <div class="brand-initials">TFP</div>
      <div class="brand-name">Thornvale Family Psychiatry</div>
    </div>
    <div class="divider"></div>
    <div class="contact">
      <div class="person-name">Daniel Harper</div>
      <div class="person-role">Director</div>
      <div class="address">2719 Alder Creek<br>Road Tampa, FL 33647</div>
      <div class="contact-line">
        <svg viewBox="0 0 16 16" aria-hidden="true"><path d="M4 1.5l2.5 3-1.5 1.8c.8 1.8 2.1 3.1 3.9 3.9l1.8-1.5 3 2.5-1.5 2.8C7 13.8 2.2 9 1.2 3z" fill="var(--brand-blue)"/></svg>
        <span>952-555-0147</span>
      </div>
      <div class="contact-line">
        <svg viewBox="0 0 16 16" aria-hidden="true"><rect x="1.5" y="3.5" width="13" height="9" fill="none" stroke="var(--brand-blue)" stroke-width="1.4"/><path d="M1.5 3.5L8 9l6.5-5.5" fill="none" stroke="var(--brand-blue)" stroke-width="1.4"/></svg>
        <span>info@thornvalefamily.com</span>
      </div>
      <div class="contact-line">
        <svg viewBox="0 0 16 16" aria-hidden="true"><g fill="none" stroke="var(--brand-blue)" stroke-width="1.3"><circle cx="8" cy="8" r="6.3"/><ellipse cx="8" cy="8" rx="2.8" ry="6.3"/><path d="M1.7 8h12.6M2.8 4.8h10.4M2.8 11.2h10.4"/></g></svg>
        <span>www.<span class="web-domain">thornvalefamily</span>.com</span>
      </div>
    </div>
  </section>
</main>
</body>
</html>
```